Harlow Chiropractic we would like to design a trifold brochure that highlights our services

We need a Trifold created for our Chiropractic offices that highlights our services and treatments that we offer giving patients a better quality of life . Areas to highlight
conditions can be found on our websites and specialties .www.harlowchiropractic.example
our doctors have over 20 years experience in this field .
they have worked with the Ridgeport falcons and Dr. Ben Harlow is the Clearwater valley college basketball teams main chiropractor.

Target Market(s)

children to elderly

Font styles to use
Serif

Colors
00a990
0255a3

Requirements
Must have
• logo
• contact info
• pics of doctors
• bios of doctors
• location
• services provided
Nice to have
• none
Should not have
• do not use picture on website of staff we have all new staff in office

```html
<!DOCTYPE html>
<html lang="en">
<head>
<meta charset="utf-8">
<title>Harlow Chiropractic – Trifold Brochure</title>
<link href="https://fonts.googleapis.com/css2?family=Roboto+Slab:wght@300;400;600&family=Source+Sans+3:wght@600&display=swap" rel="stylesheet">
<style>
  :root{
    --teal:#00a990;
    --blue:#0255a3;
    --ink:#3a3a3a;
    --paper:#ffffff;
    --backdrop:#ececec;
  }
  *{box-sizing:border-box;margin:0;padding:0}
  html,body{width:1200px;height:474px;overflow:hidden}
  body{
    background:radial-gradient(ellipse at center,#fafafa 0%,var(--backdrop) 75%);
    font-family:"Roboto Slab",Georgia,serif;
    font-weight:300;
    color:var(--ink);
  }
  .brochure{
    position:absolute;left:285px;top:15px;width:630px;height:444px;
    display:flex;box-shadow:0 6px 18px rgba(0,0,0,.25);background:var(--paper);
  }
  .panel{position:relative;width:210px;height:444px;overflow:hidden}
  .photo{position:absolute;left:0;width:210px}
  .band{position:absolute;left:0;width:210px}
  .heading{
    position:absolute;font-family:"Source Sans 3",Arial,sans-serif;font-weight:600;
    color:var(--blue);letter-spacing:-.2px;line-height:1;white-space:nowrap;
  }
  .copy{position:absolute;font-size:7.2px;line-height:9.6px}
  .copy p{margin-bottom:7px}
  .copy a{color:var(--blue);text-decoration:none}

  /* Panel 1 */
  .panel--intro .photo{top:0;height:122px;background:linear-gradient(120deg,#e6e2dc 0%,#d9c7b4 45%,#e48a2c 60%,#8c8c8c 100%)}
  .panel--intro .heading{left:32px;top:116px;font-size:29px}
  .panel--intro .copy{left:10px;top:146px;width:195px}
  .wrap-circle{float:right;width:150px;height:300px;shape-outside:circle(142px at 159px 220px)}
  .ring{position:absolute;left:0;top:0}
  .doctors-circle{position:absolute;left:80px;top:276px;width:127px;height:175px;
    font-size:7.2px;line-height:9.6px;color:#fff;text-align:right}
  .doctors-circle .edge{float:left;width:80px;height:175px;
    shape-outside:polygon(0 0,39px 0,22px 30px,14px 73px,20px 110px,35px 140px,52px 160px,73px 175px,0 175px)}

  /* Panel 2 */
  .panel--bio{background:var(--teal);color:#fff}
  .panel--bio .copy{left:12px;top:6px;width:190px;text-align:justify;line-height:9.7px}
  .doctor-photo{float:left;width:48px;height:64px;margin:2px 6px 2px 0;
    background:linear-gradient(180deg,#dfe3e6 0%,#c9ced3 55%,#3c4656 100%);border:1px solid #fff}
  .doctor-name{font-weight:600;font-size:7.6px}

  /* Panel 3 */
  .panel--relief .photo--top{top:0;height:128px;background:linear-gradient(90deg,#111 0%,#4a4543 45%,#b9b2ad 70%,#3a3532 100%)}
  .panel--relief .photo--bottom{top:366px;height:78px;background:linear-gradient(120deg,#1a1716 0%,#6e5a50 45%,#3a2e2a 100%)}
  .heading--back{left:10px;top:130px;font-size:25px}
  .heading--neck{left:10px;top:236px;font-size:25px}
  .copy--back{left:10px;top:156px;width:195px}
  .copy--neck{left:10px;top:262px;width:195px}
  .contact{position:absolute;left:10px;top:330px;width:195px;font-size:7.2px;line-height:9.6px}
  .brand{display:flex;align-items:center;gap:4px;font-weight:600;font-size:8.6px;color:var(--blue);line-height:11px}
  .brand-dot{width:7px;height:7px;border-radius:50%;background:var(--teal)}
  .contact-web{color:var(--blue)}
</style>
</head>
<body>
<main class="brochure">

  <section class="panel panel--intro">
    <div class="photo" role="img" aria-label="Smiling woman exercising on a stationary bike"></div>
    <svg class="band" style="top:96px" width="210" height="34" viewBox="0 0 210 34" aria-hidden="true">
      <path d="M0 16 Q105 -6 210 6 L210 34 L0 34 Z" fill="var(--blue)"/>
      <path d="M0 24 Q105 4 210 14 L210 34 L0 34 Z" fill="#fff"/>
    </svg>
    <h1 class="heading">Chiropractic</h1>
    <div class="copy">
      <div class="wrap-circle"></div>
      <p>Dr. Ben Harlow has been providing chiropractic care to people in Ridgeport for many years, and we hear from many people who have never been to a chiropractor. If you've never had chiropractic care, you might be surprised about how it can help you improve your health.</p>
      <p>Chiropractic was first developed in the 1890s, and it works by restoring the normal and <a href="#">healthy functioning of your central nervous system</a> by adjusting the spine. The term "chiropractic" originates with the Greek words "chiro" and "praktikos," which mean "hand" and "practice." Your <a href="#">Ridgeport chiropractor</a> helps you by using natural, hands-on care that doesn't involve risky drugs or surgery.</p>
      <p>You're probably aware of some of the <a href="#">benefits of chiropractic care</a>, such as back pain or neck pain relief. But did you know that chiropractic can also help with general health and wellness?</p>
    </div>
    <svg class="ring" width="210" height="444" aria-hidden="true">
      <circle cx="214" cy="366" r="132" fill="none" stroke="var(--teal)" stroke-width="3"/>
      <circle cx="214" cy="366" r="127" fill="var(--blue)"/>
    </svg>
    <div class="doctors-circle">
      <div class="edge"></div>
      Dr. Ben Harlow &amp; Dr. Jon Harlow, your Ridgeport Chiropractors and Westbrook College of Chiropractic graduates, provide quality chiropractic care to patients in Ridgeport. If you suffer from back pain, neck pain, headache, sciatica or have been in an auto collision, Harlow Chiropractic can get you back on the road to health.
    </div>
  </section>

  <section class="panel panel--bio">
    <div class="copy">
      <div class="doctor-photo" role="img" aria-label="Portrait of Dr. Ben Harlow in shirt and tie"></div>
      <p><span class="doctor-name">Dr. Ben Harlow</span><br>
      Since Dr. Harlow was old enough to dream, he knew that he wanted to be a chiropractor. After attending Westbrook College of Chiropractic and fueling his career in chiropractic with the mindset of putting patients first, he has made the dream of one day owning his own clinic here in Ridgeport a reality. Keeping a compassionate and supportive mentality, Dr. Ben is very attentive toward each and every patient, allocating a vast range of therapies so that each patient leaves feeling rejuvenated. Not only is Dr. Ben very knowledgeable and experienced, but patients understand after seeing him that it really is all about them. Dr. Harlow has a plan for each of his individual patients that exceeds the lengths many chiropractors fail to maintain because he drives himself to direct and lasting results for his patients.</p>
      <p>"No one leaves this clinic feeling like a number," comments Dr. Ben when asked what he feels sets his clinic apart from all the others in Ridgeport. "I don't want you to only feel better for a day after you see me. I want you, as my patient, to feel better indefinitely by receiving a successful wellness plan that I have specifically designed for you. Every person that walks through these doors is different. What works for some may not work for others. My goal is to promote healthy habits along with patient therapies so that pain will not be an option."</p>
      <p>This is the difference Harlow Chiropractic brings to the table. Long-lasting results you can feel make every visit seem like a day at the spa. This clinic offers the latest technology so troubled areas are spotted quickly and eliminated. So, come see Dr. Ben and find a plan for wellness. Dr. Ben believes in not only having sympathy for his patients, but more importantly, he has empathy. All of the public, children, and walk-ins are welcomed!</p>
    </div>
  </section>

  <section class="panel panel--relief">
    <div class="photo photo--top" role="img" aria-label="Close-up of a bare shoulder with a red highlight marking back pain"></div>
    <svg class="band" style="top:106px" width="210" height="26" viewBox="0 0 210 26" aria-hidden="true">
      <path d="M0 8 Q110 -4 210 10 L210 26 L0 26 Z" fill="var(--blue)"/>
      <path d="M0 16 Q110 6 210 18 L210 26 L0 26 Z" fill="#fff"/>
    </svg>
    <h2 class="heading heading--back">Back Pain Relief</h2>
    <div class="copy copy--back">
      <p>If you suffer from back pain, we can help. Dr. Ben Harlow has been helping people in Ridgeport recover from back pain for many years.</p>
      <p>There can be many different causes of back pain, but Dr. Ben Harlow will first identify the root cause of your pain and then determine the best way to help you recover.</p>
    </div>
    <h2 class="heading heading--neck">Neck Pain Relief</h2>
    <div class="copy copy--neck">
      <p>Neck pain is a common problem in our society, and Dr. Ben Harlow is here to help. Neck pain can be caused from work or auto injuries, poor posture, or just everyday stress and strains.</p>
      <p>At Harlow Chiropractic, we've helped many patients in Ridgeport recover from neck pain, no matter the cause.</p>
    </div>
    <div class="contact">
      <div class="brand"><span class="brand-dot"></span>Harlow Chiropractic</div>
      <div class="contact-web">www.harlowchiropractic.example</div>
    </div>
    <div class="photo photo--bottom" role="img" aria-label="Person holding the back of their neck in pain"></div>
    <svg class="band" style="top:356px" width="210" height="22" viewBox="0 0 210 22" aria-hidden="true">
      <path d="M0 0 L210 0 L210 6 Q100 20 0 10 Z" fill="#fff"/>
      <path d="M0 10 Q100 20 210 6 L210 12 Q100 26 0 15 Z" fill="var(--blue)"/>
    </svg>
  </section>

</main>
</body>
</html>
```